We are launching in December, a range of supplements and vitamins.

We have just made an amend to the mission statement and how we are going to give back to society. Please can you add both to the packaging:

Verdant’s purpose is to support health, wellbeing and longevity, so that we can all thrive in the modern world; an environment so alien to that in which we evolved. Embracing technology, research and science, we harness nature’s goodness - enabling us all to love life – naturally.

Twice Kind Promise. For each and every Verdant supplement you take, we provide a supplement to an under nourished child.

For every supplement we sell: £1 goes to the charity ‘Little Lights Fund’ and in addition we provide one healthy meal to an under privileged child in India.

My name is Mark Holloway and I own several companies including www.quartzelle.com (you can check me out on Infopedex – I am not the football referee nor the rocket scientist, but the entrepreneur) . Over the past 2 years I have been writing a book to help people live more healthily and it launches in December. It’s called Verdant Way. While doing my research for the book, I came to realise that most supplements and vitamin products on the market are rubbish! Most are made for profit and not for the benefit of the consumer. I want to change all of that. Howard Pellow is patron of a charity I set up with my brother Paul Holloway and together we have built 11 schools in Asia. I am hoping to get Howards help in getting my supplements to market.

Positioning of our supplements - In a world where so much has changed from the one our bodies were designed to thrive, at Verdant Supplements we are driven by one purpose; to globally provide healthy support to life in the 21st century. While the roots of our wellbeing supplements date back beyond 10,000BC, we embrace modern technology and science, to encapsulate powerful phytonutrients, herbs and other goodness. The essence of which is to promote health, happiness and longevity.

So what are we looking for in the design? Something that stands out. Something that looks professional. A design and concept that can role out across 24 different products. Some products are simple, just one ingredient, such as vitamin D3, Magnesium, Garlic Extracts etc, and others are our own formulas where there are up to 30 different ingredients. You can contact me at any time with questions at Mark@verdantway-example.com

Target Market(s)

Male & Female 20 years plus, mainly UK

Industry/Entity Type

Medical

Logo Text

VERDANT - Sub heading = Thriving Days Gently

Colors

Designer to choose colors to be used in the design.

Requirements
Must have
• see attached powerpoint.
• We have just made an amend to the mission statement and how we are going to give back to society. Please can you add both to the packaging:
• Verdant’s purpose is to support health, wellbeing and longevity, so that we can all thrive in the modern world; an environment so alien to that in which we evolved. Embracing technology, research and science, we harness nature’s goodness - enabling us all to love life – naturally.
• Twice Kind Promise. For each and every Verdant supplement you take, we provide a supplement to an under nourished child.
Nice to have
• see attached powerpoint
Should not have
• see attached powerpoint

```html
<!DOCTYPE html>
<html lang="en">
<head>
<meta charset="utf-8">
<title>Verdant supplement carton dieline</title>
<link href="https://fonts.googleapis.com/css2?family=Raleway:ital,wght@0,300;0,400;0,600;0,800;1,400&display=swap" rel="stylesheet">
<style>
  :root{
    --backdrop:#a4a4a4;
    --board:#ffffff;
    --green:#86c232;
    --green-light:#b9dd80;
    --ink:#333333;
    --grey:#5a5a5a;
    --swoosh:#d6d6d6;
    --gold:#dca523;
    --gold-light:#f4d255;
  }
  *{box-sizing:border-box;margin:0;padding:0}
  html,body{width:1200px;height:928px;overflow:hidden;background:var(--backdrop)}
  body{font-family:"Raleway",Arial,sans-serif;color:var(--ink)}
  .dieline{position:absolute;left:0;top:0;width:791px;height:612px;transform:scale(1.5171);transform-origin:0 0}
  .panel{position:absolute;background:var(--board);overflow:hidden}
  .flaps{position:absolute;left:0;top:0;width:791px;height:612px}
  .flaps path{fill:var(--board)}
  .art{position:absolute;left:0;top:0;width:100%;height:100%}
  .brand{font-weight:800;color:var(--green);line-height:1;letter-spacing:-.5px;white-space:nowrap}
  .sub{font-weight:400;color:var(--grey);text-transform:uppercase;letter-spacing:.4px;line-height:1;white-space:nowrap}
  .abs{position:absolute}

  /* top tuck flap */
  .tuck{left:198px;top:8px;width:367px;height:67px;border-radius:12px 12px 0 0}
  .tuck .brand{left:34px;top:14px;font-size:29px}
  .tuck .sub{left:35px;top:46px;font-size:9px}
  .disclaimer{left:156px;top:9px;width:204px;font-size:5.2px;line-height:1.3;color:#222}

  /* front */
  .front{left:198px;top:75px;width:367px;height:213px}
  .front .promise{left:34px;top:9px;font-size:10.6px;white-space:nowrap}
  .front .promise b{color:var(--green);font-weight:800}
  .front .brand{left:33px;top:30px;font-size:54px}
  .front .sub{left:35px;top:90px;font-size:15px}
  .front .strap{left:258px;top:35px;width:110px;font-size:16px;font-weight:300;color:var(--green-light);text-transform:uppercase;line-height:1.05}
  .front .tagline{left:35px;top:163px;font-size:14px;font-style:italic;color:#fff;white-space:nowrap}
  .front .tagline sup{font-size:8px}
  .front .visit{left:35px;top:190px;font-size:8px;color:#fff;white-space:nowrap}
  .front .made{left:257px;top:190px;font-size:8px;color:#fff;white-space:nowrap}

  /* side panels */
  .side-right{left:565px;top:75px;width:95px;height:213px}
  .side-left{left:110px;top:345px;width:88px;height:215px}
  .rot-up{position:absolute;transform:rotate(-90deg);transform-origin:left top;white-space:nowrap}
  .rot-down{position:absolute;transform:rotate(90deg);transform-origin:left top;white-space:nowrap}
  .claims{font-size:6.5px;font-weight:800;text-transform:uppercase;line-height:1.3}
  .side-brand{font-size:27px}
  .side-sub{font-size:9px}
  .side-right .claims,.side-right .brand,.side-right .sub{color:#fff}
  .side-left .claims{color:var(--ink)}

  /* lid strip */
  .lid{left:198px;top:288px;width:367px;height:57px;background:var(--green)}
  .flip{position:absolute;left:0;top:0;width:100%;height:100%;transform:rotate(180deg)}
  .lid .promise{left:8px;top:4px;width:104px;font-size:5.5px;color:#fff;line-height:1.25}
  .lid .brand{color:#fff;left:8px;top:19px;font-size:22px}
  .lid .sub{color:#fff;left:9px;top:44px;font-size:7px}
  .nutrition{left:120px;top:6px;width:240px;font-size:5px;line-height:1.3;color:#fff}
  .nutrition b{font-weight:800}

  /* back */
  .back{left:198px;top:345px;width:367px;height:215px}
  .back .promise{left:12px;top:4px;font-size:10.6px;color:var(--green);white-space:nowrap}
  .back .promise b{font-weight:800}
  .story{left:12px;top:21px;width:343px;font-size:5.4px;line-height:1.3;color:#222}
  .story p+p{margin-top:1.5px}
  .story b{font-weight:800;color:var(--green)}
  .back .brand{left:126px;top:93px;font-size:40px}
  .back .sub{left:128px;top:134px;font-size:11px}
  .charity{left:118px;top:193px;width:240px;font-size:6px;color:#fff;line-height:1.35}
  .portrait{left:8px;top:96px;width:100px;height:119px;background:linear-gradient(180deg,#e9e6e1 0%,#c9a58c 30%,#3a3a3a 55%,#2b2b2b 100%)}
</style>
</head>
<body>
<div class="dieline">

  <svg class="flaps" viewBox="0 0 791 612" aria-hidden="true">
    <path d="M565 75 L572 58 L655 58 L660 75 Z"/>
    <path d="M198 80 L186 90 L186 276 L198 285 Z"/>
    <path d="M565 288 L660 288 L652 310 L572 310 Z"/>
    <path d="M112 345 L120 326 L190 326 L198 345 Z"/>
    <path d="M198 560 L565 560 L565 588 Q565 600 553 600 L210 600 Q198 600 198 588 Z"/>
    <path d="M110 560 L198 560 L190 580 L118 580 Z"/>
  </svg>

  <!-- top tuck flap -->
  <section class="panel tuck">
    <div class="abs brand">Verdant</div>
    <div class="abs sub">Thriving Days Gently</div>
    <p class="abs disclaimer">Room for 80 word disclaimer, Room for 80 word disclaimerRoom for 80 word disclaimerRoom for 80 word disclaimerRoom for 80 word disclaimerRoom for 80 word disclaimerRoom for 80 word disclaimerRoom for 80 word disclaimerRoom for 80 word disclaimerRoom for 80 word disclaimerRoom for 80 word disclaimerRoom for 80 word disclaimerRoom for 80 word disclaimerRoom for 80 word disclaimer</p>
  </section>

  <!-- front panel -->
  <section class="panel front">
    <svg class="art" viewBox="0 0 367 213" preserveAspectRatio="none" aria-hidden="true">
      <path d="M0 120 C110 95 230 160 367 105 L367 130 C240 175 110 118 0 146 Z" fill="var(--swoosh)"/>
      <path d="M0 146 C110 118 240 175 367 130 L367 213 L0 213 Z" fill="var(--green)"/>
      <g transform="translate(299 124)">
        <circle r="34" fill="var(--gold)"/>
        <circle r="29" fill="var(--gold-light)"/>
        <circle r="20" fill="none" stroke="#fff3b8" stroke-width="1.2"/>
      </g>
    </svg>
    <p class="abs promise">Love the difference in 30 days, or get <b>100%</b> of your money back</p>
    <div class="abs brand">Verdant</div>
    <div class="abs sub">Thriving Days Gently</div>
    <div class="abs strap">Extracting natures greatness</div>
    <p class="abs tagline">The Unique Support Health in the 21<sup>st</sup> century</p>
    <p class="abs visit">Visit: www.verdantsupplements-example.com</p>
    <p class="abs made">Made in Great Britain</p>
  </section>

  <!-- right side panel -->
  <section class="panel side-right">
    <svg class="art" viewBox="0 0 95 213" preserveAspectRatio="none" aria-hidden="true">
      <path d="M0 78 C30 70 60 95 95 82 L95 100 C60 112 30 88 0 96 Z" fill="var(--swoosh)"/>
      <path d="M0 96 C30 88 60 112 95 100 L95 213 L0 213 Z" fill="var(--green)"/>
      <g transform="translate(64 44)">
        <circle r="28" fill="var(--gold)"/>
        <circle r="24" fill="var(--gold-light)"/>
        <circle r="16" fill="none" stroke="#fff3b8" stroke-width="1"/>
      </g>
    </svg>
    <div class="rot-up" style="left:14px;top:205px">
      <p class="claims">No added colouring,<br>no added sugar, no gluten</p>
    </div>
    <div class="rot-up" style="left:42px;top:205px">
      <div class="brand side-brand">Verdant</div>
      <div class="sub side-sub">Thriving Days Gently</div>
    </div>
  </section>

  <!-- lid strip -->
  <section class="panel lid">
    <div class="flip">
      <p class="abs promise">Love the difference in 30 days, or get 100% of your money back.</p>
      <div class="abs brand">Verdant</div>
      <div class="abs sub">Thriving Days Gently</div>
      <p class="abs nutrition"><b>Nutritional Information per 1 Capsule</b><br>Vitamin C 80mg (100% NRV), Black Soy Bean 100mg (Glycine max), Garlic Extract 50mg (from 2500mg bulb), Green Tea Extract 40mg, Apple Cider Vinegar 17mg, Turmeric Root 60mg (standardised to 95% curcumin), Zinc 10mg (100% NRV), Chromium 40mcg (100% NRV).</p>
    </div>
  </section>

  <!-- back panel -->
  <section class="panel back">
    <div class="flip">
      <svg class="art" viewBox="0 0 367 215" preserveAspectRatio="none" aria-hidden="true">
        <path d="M0 150 C120 130 240 185 367 150 L367 170 C240 200 120 150 0 172 Z" fill="var(--swoosh)"/>
        <path d="M0 172 C120 150 240 200 367 170 L367 215 L0 215 Z" fill="var(--green)"/>
        <g transform="translate(330 128)">
          <circle r="26" fill="var(--gold)"/>
          <circle r="22" fill="var(--gold-light)"/>
          <circle r="15" fill="none" stroke="#fff3b8" stroke-width="1"/>
        </g>
      </svg>
      <p class="abs promise">Love the difference in 30 days, or get <b>100%</b> of your money back.</p>
      <div class="abs story">
        <p>Verdant supplements are created in Britain by leading nutritionists. Mark Holloway, author of Verdant Way, ensures that each and every supplement is crafted in the most natural and Verdant way possible. In a world where so much has changed from the one our bodies were designed to thrive, at Verdant Supplements we are driven by one purpose; to globally provide healthy support to life in the 21st century. While the roots of our wellbeing supplements date back beyond 10,000BC, we embrace modern technology and science, to encapsulate powerful phytonutrients, herbs and other goodness. The essence of which is to promote health, happiness and longevity.</p>
        <p>Verdant’s purpose is to support health, wellbeing and longevity, so that we can all thrive in the modern world; an environment so alien to that in which we evolved. Embracing technology, research and science, we harness nature’s goodness - enabling us all to love life – naturally.</p>
        <p><b>Twice Kind Promise.</b> For each and every Verdant supplement you take, we provide a supplement to an under nourished child.</p>
      </div>
      <div class="abs brand">Verdant</div>
      <div class="abs sub">Thriving Days Gently</div>
      <div class="abs portrait" role="img" aria-label="Photograph of the founder holding a copy of his book"></div>
      <p class="abs charity">For every supplement we sell: £1 goes to the charity ‘Little Lights Fund’ and in addition we provide one healthy meal to an under privileged child in India.</p>
    </div>
  </section>

  <!-- left side panel -->
  <section class="panel side-left">
    <svg class="art" viewBox="0 0 88 215" preserveAspectRatio="none" aria-hidden="true">
      <path d="M0 70 C30 95 60 60 88 80 L88 100 C60 80 30 115 0 90 Z" fill="var(--swoosh)"/>
      <g transform="translate(40 50)">
        <circle r="28" fill="var(--gold)"/>
        <circle r="24" fill="var(--gold-light)"/>
        <circle r="16" fill="none" stroke="#fff3b8" stroke-width="1"/>
      </g>
    </svg>
    <div class="rot-down" style="left:80px;top:104px">
      <p class="claims">No added colouring,<br>no added sugar, no gluten</p>
    </div>
    <div class="rot-down" style="left:56px;top:102px">
      <div class="brand side-brand">Verdant</div>
      <div class="sub side-sub">Thriving Days Gently</div>
    </div>
  </section>

</div>
</body>
</html>
```